Namecard Designs+Logo for a High End Automobile Company

We need a new business card for our company called Velta Motorhof.

www.veltamotorhof.example.sg
Our new website will be up in 2.5 months time.

We sell used and brand new continental cars like Korvane, QTL, Dravell, Solbrini and etc. Currently we are operating from 2 offices in Singapore and United Kingdom.

We want a design which is serious. We are open to colours but try to keep it at a maximum of 3 colours.

We prefer something simple and minimal. We are open to 2 sides printing or even 2 sided namecards. Both UK and Singapore company offices address must be in; either side by side, front and back, or even 2 sided cards.

The logo can be a text logo, emblem, abstract, pictorial or combination.

We are printing with Pribo.com so please kindly follow the printing guideline.

http://uk.pribo.example/help/faq/templates-and-guidelines.html

Rich and Car Enthusiasts

Printing

Must have
• Our 2 offices; UK and Singapore.

Our slogan which is " The Automobile Specialist"
Should not have
• Not more than 3 colours

```html
<!DOCTYPE html>
<html lang="en">
<head>
<meta charset="utf-8">
<title>Velta Motorhof – Business Cards</title>
<link href="https://fonts.googleapis.com/css2?family=Source+Sans+3:wght@300;400;600&display=swap" rel="stylesheet">
<style>
  :root {
    --backdrop: #d6d6d6;
    --card-core: #0f3150;
    --card-mid: #0a1f33;
    --card-edge: #040a12;
    --text-light: #d3dce5;
    --accent-blue: #1fa3d8;
    --brand-silver: #e4e8ec;
  }
  * { margin: 0; padding: 0; box-sizing: border-box; }
  html, body {
    width: 1200px;
    height: 899px;
    overflow: hidden;
    background: var(--backdrop);
    font-family: "Source Sans 3", "Myriad Pro", sans-serif;
  }
  .card {
    position: absolute;
    width: 580px;
    height: 331px;
    border-radius: 22px;
    background: radial-gradient(ellipse 60% 75% at 50% 40%, var(--card-core) 0%, var(--card-mid) 55%, var(--card-edge) 100%);
    box-shadow: 0 4px 14px rgba(0, 0, 0, 0.25);
    color: var(--text-light);
  }
  .card-front { left: 297px; top: 123px; }
  .card-back {
    left: 309px; top: 481px;
    background: radial-gradient(ellipse 60% 80% at 62% 45%, var(--card-core) 0%, var(--card-mid) 55%, var(--card-edge) 100%);
  }

  .brand { position: absolute; text-align: center; }
  .brand-name {
    font-weight: 600;
    font-size: 31px;
    line-height: 1;
    color: var(--brand-silver);
    letter-spacing: 0.5px;
  }
  .brand-slogan {
    margin-top: 6px;
    font-weight: 600;
    font-size: 14px;
    letter-spacing: 2.2px;
    color: #ffffff;
  }
  .card-front .brand { left: 0; right: 0; top: 165px; }
  .card-back .brand { right: 28px; top: 262px; }

  .offices {
    position: absolute;
    left: 0; right: 0; top: 274px;
    text-align: center;
    font-weight: 300;
    font-size: 14.5px;
    line-height: 20px;
  }
  .offices .phone { margin-left: 10px; }

  .contact { position: absolute; left: 29px; top: 48px; }
  .person-name {
    font-weight: 600;
    font-size: 20px;
    color: var(--accent-blue);
    line-height: 24px;
  }
  .person-role {
    font-weight: 300;
    font-size: 16px;
    line-height: 22px;
  }
  .details {
    margin-top: 20px;
    list-style: none;
    font-weight: 300;
    font-size: 14px;
    line-height: 22px;
  }
  .details b { font-weight: 600; margin-right: 4px; }
  .details .web { letter-spacing: 0.8px; }
</style>
</head>
<body>
  <section class="card card-front">
    <div class="brand">
      <div class="brand-name">Velta Motorhof</div>
      <div class="brand-slogan">The Automobile Specialist</div>
    </div>
    <div class="offices">
      <p>United Kingdom . 8 Marlow Quay <span class="phone">416 555 0148</span></p>
      <p>Singapore. 8 Marlow Quay <span class="phone">416 555 0148</span></p>
    </div>
  </section>

  <section class="card card-back">
    <div class="contact">
      <h1 class="person-name">Lena Varro</h1>
      <p class="person-role">Marketing Manager</p>
      <ul class="details">
        <li><b>P.</b> 416 555 0148</li>
        <li><b>E.</b> lvarro@veltamotorhof.example.sg</li>
        <li class="web">www.veltamotorhof.example.sg</li>
      </ul>
    </div>
    <div class="brand">
      <div class="brand-name">Velta Motorhof</div>
      <div class="brand-slogan">The Automobile Specialist</div>
    </div>
  </section>
</body>
</html>
```